Business Card Design Project

I need a business card design for our new logo, please check the logo at the following link:
https://files.quorvane-share.com/s/p7tkwe3nq4zr81h/FernCove.png
The address on the business card:
Av. Olegário Tavares 418 sala 207
Barra da Tijuca, Rio de Janeiro, RJ
CEP: 24917-380
Brasil
Phone: +55 21 73408216
e-mail: rogerio@ferncove-exemplo.com.br
Updates
Thank you all for sending your designs, we will not provide feedback because there are too many designs, on December 3 we will pick the best design according to our point of view. Please keep posting.
Rogério
Industry/Entity Type
Business

```html
<!DOCTYPE html>
<html lang="pt-BR">
<head>
<meta charset="utf-8">
<title>FernCove – Cartão de visita</title>
<link rel="stylesheet" href="https://fonts.googleapis.com/css2?family=Cabin:wght@400;700&display=swap">
<style>
  :root {
    --navy-deep: #000d2a;
    --navy-mid: #1b3a66;
    --navy-edge: #020f2c;
    --gold-band: #8a5e1f;
    --yellow: #f4c418;
    --lilac: #ecc8ea;
    --silhouette: #0b2236;
  }
  html, body {
    margin: 0;
    padding: 0;
    width: 1200px;
    height: 736px;
    overflow: hidden;
    background: var(--navy-deep);
  }
  .card {
    position: relative;
    width: 1200px;
    height: 736px;
    font-family: "Cabin", sans-serif;
    overflow: hidden;
  }
  .card__top {
    position: absolute;
    left: 0; top: 0;
    width: 1200px; height: 493px;
    background: radial-gradient(ellipse 70% 75% at 50% 45%, var(--navy-mid) 0%, #12294f 55%, var(--navy-edge) 100%);
  }
  .card__band {
    position: absolute;
    left: 0; top: 493px;
    width: 1200px; height: 92px;
    background: var(--gold-band);
  }
  .card__bottom {
    position: absolute;
    left: 0; top: 585px;
    width: 1200px; height: 151px;
    background: var(--navy-deep);
  }
  .mascot-area {
    position: absolute;
    left: 84px; top: 24px;
    width: 350px; height: 300px;
    border-radius: 40px;
    background: radial-gradient(ellipse at 50% 50%, rgba(11,34,54,0.85) 0%, rgba(11,34,54,0.35) 70%, rgba(11,34,54,0) 100%);
  }
  .brand-name {
    position: absolute;
    left: 70px; top: 318px;
    margin: 0;
    font-size: 112px;
    font-weight: 700;
    line-height: 1;
    letter-spacing: -2px;
    color: var(--yellow);
  }
  .address {
    position: absolute;
    left: 531px; top: 138px;
    margin: 0;
    font-style: normal;
    font-size: 31px;
    line-height: 48px;
  }
  .address span { display: block; }
  .address .lilac { color: var(--lilac); }
  .address .gold { color: var(--yellow); }
  .contact {
    position: absolute;
    left: 67px;
    display: flex;
    align-items: center;
    color: var(--lilac);
    font-size: 31px;
  }
  .contact svg { display: block; flex: none; }
  .contact--email { top: 610px; }
  .contact--email span { margin-left: 19px; }
  .contact--phone { top: 666px; }
  .contact--phone span { margin-left: 29px; }
</style>
</head>
<body>
<div class="card">
  <div class="card__top"></div>
  <div class="card__band"></div>
  <div class="card__bottom"></div>

  <div class="mascot-area" role="img" aria-label="Ilustração da mascote da marca correndo com uma maleta"></div>
  <p class="brand-name">FernCove</p>

  <address class="address">
    <span class="lilac">Av. Olegário Tavares 418 sala 207</span>
    <span class="gold">Barra da Tijuca, Rio de Janeiro, RJ</span>
    <span class="lilac">CEP: 24917-380</span>
    <span class="gold">Brasil</span>
  </address>

  <div class="contact contact--email">
    <svg width="45" height="36" viewBox="0 0 45 36" aria-hidden="true">
      <rect x="1.5" y="1.5" width="42" height="33" fill="none" stroke="#ffffff" stroke-width="2.5"/>
      <polyline points="1.5,1.5 22.5,20 43.5,1.5" fill="none" stroke="#ffffff" stroke-width="2.5"/>
      <line x1="1.5" y1="34.5" x2="17" y2="16" stroke="#ffffff" stroke-width="2.5"/>
      <line x1="43.5" y1="34.5" x2="28" y2="16" stroke="#ffffff" stroke-width="2.5"/>
    </svg>
    <span>rogerio@ferncove-exemplo.com.br</span>
  </div>

  <div class="contact contact--phone">
    <svg width="45" height="40" viewBox="0 0 45 40" aria-hidden="true">
      <path d="M2 12 C2 2 43 2 43 12 L43 15 L33 15 L33 10 C28 8 17 8 12 10 L12 15 L2 15 Z" fill="#ffffff"/>
      <path d="M10 17 L35 17 L42 38 L3 38 Z" fill="#ffffff"/>
      <circle cx="22.5" cy="27" r="6" fill="#000d2a"/>
      <circle cx="22.5" cy="27" r="2.5" fill="#ffffff"/>
    </svg>
    <span>+55 21 73408216</span>
  </div>
</div>
</body>
</html>
```